Landscape Contractor in need of New Web Design

HELP.. Please Help!!!!. Our current website is old, outdated, ugly... and well nothing like us.... so we are looking for someone to help build a new website that fits our company direction. We are a landscape company with multiple locations in order to meet the needs of our clients and their projects throughout the midwest. When most people think of landscaping, they think of mowing grandmas yard, but that is NOT even remotely close to what we do. We are 100% a commercial landscape company meaning we complete landscape and irrigation services for large scale commercial projects. We are looking for a website to showcase our commercial talents and awesome team of people.
Updates

Address of current website is www.plovermeadowco.com

```html
<!DOCTYPE html>
<html lang="en">
<head>
<meta charset="utf-8">
<title>Plover Meadow — Commercial Landscaping</title>
<link href="https://fonts.googleapis.com/css2?family=Rubik:wght@500;600;700&family=Work+Sans:wght@400;500;600;700&display=swap" rel="stylesheet">
<style>
:root{
  --forest:#063306;
  --forest-2:#0d4a0c;
  --green:#1f8a0e;
  --lime:#6fe01c;
  --lime-dark:#4fb80f;
  --orange:#eea53a;
  --ink:#2b2b2b;
  --muted:#7a7f7a;
  --mist:#f1f4f1;
  --line:#e4e8e4;
  --white:#ffffff;
}
*{box-sizing:border-box;margin:0;padding:0}
html,body{width:1200px;height:4819px;overflow:hidden}
body{position:relative;background:var(--white);font-family:"Work Sans",sans-serif;color:var(--ink)}
.abs{position:absolute}
h1,h2,h3,.heading{font-family:"Rubik",sans-serif;font-weight:700}
.eyebrow{font-size:7px;letter-spacing:1.6px;font-weight:700;text-transform:uppercase;color:var(--orange)}
.btn{display:inline-flex;align-items:center;justify-content:center;background:var(--lime);color:var(--forest);font-size:7px;letter-spacing:1.4px;font-weight:700;text-transform:uppercase}
.photo{position:absolute}
p.body{font-size:10px;line-height:16px;color:var(--muted)}

/* admin bar */
.admin-bar{top:0;left:0;width:1200px;height:17px;background:#1d2327;color:#dcdcdc;font-size:8px;display:flex;align-items:center;padding:0 10px;gap:16px}
.admin-bar .right{margin-left:auto}

/* header */
.site-header{top:17px;left:0;width:1200px;height:58px;background:var(--white)}
.brand{position:absolute;left:243px;top:10px;height:38px;display:flex;align-items:center;gap:6px;font-family:"Rubik",sans-serif;font-weight:700;font-size:13px;color:var(--forest)}
.brand .dot{width:14px;height:14px;border-radius:50%;background:var(--lime)}
.nav{position:absolute;left:363px;top:24px;display:flex;gap:14px;font-size:9px;font-weight:500}
.nav .active{color:var(--green)}
.header-phone{position:absolute;left:702px;top:24px;font-size:9px;color:var(--muted);display:flex;gap:5px;align-items:center}
.header-cta{position:absolute;left:818px;top:15px;width:125px;height:28px;border:2px solid var(--green)}

/* hero */
.hero{top:75px;left:0;width:1200px;height:520px;background:linear-gradient(180deg,#3c5f3a 0%,#4a7a3a 45%,#2f6a1a 75%,#1f5510 100%)}
.hero-title{top:150px;width:1200px;text-align:center;color:var(--white);font-size:33px;line-height:38px}
.hero-sub{top:240px;width:1200px;text-align:center;color:#e3ece0;font-size:9px}
.hero-btns{top:275px;left:489px;display:flex;gap:11px}
.hero-btns span{width:107px;height:28px}
.hero-btns .ghost{background:transparent;border:1px solid var(--lime);color:var(--lime)}
.hero-band{top:560px;left:0;width:1200px;height:35px;background:var(--green)}

/* quick contact */
.quick{top:522px;left:249px;width:702px;height:153px;background:var(--white);box-shadow:0 8px 24px rgba(0,0,0,.08)}
.quick-call{position:absolute;left:0;top:0;width:245px;height:153px;background:var(--forest);color:var(--white);text-align:center;padding-top:32px}
.quick-call .label{font-family:"Rubik",sans-serif;font-weight:700;font-size:19px;color:var(--lime);margin-top:8px}
.quick-call .num{font-size:12px;margin-top:4px}
.field{position:absolute;height:24px;background:#eef1ee;font-size:7px;color:#9aa09a;padding:0 8px;display:flex;align-items:center}
.quick .note{position:absolute;left:272px;top:116px;font-size:7.5px;color:var(--muted);padding-left:12px;border-left:2px solid var(--orange)}
.quick .rule{position:absolute;left:272px;right:28px;top:104px;border-top:1px solid var(--line)}

/* about */
.about-text{left:296px;top:796px;width:250px}
.about-text h2{font-size:22px;line-height:27px;color:var(--green);margin:10px 0 14px}
.about-text .btn{width:97px;height:22px;margin-top:22px}

/* team */
.team{top:1104px;left:0;width:1200px;height:445px;background:var(--mist)}
.team-text{left:733px;top:1228px;width:215px}
.team-text h2{font-size:22px;line-height:27px;color:var(--green);margin:10px 0 12px}
.team-text .btn{width:95px;height:22px;margin-top:22px}

/* services */
.section-head{width:1200px;text-align:center}
.section-head h2{font-size:21px;color:var(--green);margin-top:10px}
.service{position:absolute;width:159px;height:152px;background:var(--white);box-shadow:0 3px 14px rgba(0,0,0,.07);padding:14px 17px}
.service svg{width:22px;height:22px}
.service h3{font-size:12px;color:var(--green);margin:12px 0 8px}
.service p{font-size:7.5px;line-height:11px;color:var(--muted)}

/* offer */
.offer{top:2301px;left:0;width:1200px;height:554px;background:linear-gradient(100deg,#4c8a2a 0%,#2c6314 40%,#0f3a0a 100%)}
.offer-box{top:2610px;left:601px;width:355px;height:200px;border:2px solid var(--lime);padding:30px 32px}
.offer-box h2{font-size:19px;line-height:26px;color:var(--white);margin:8px 0 10px}
.offer-box p{font-size:8.5px;line-height:13px;color:#cfe0c8}
.offer-box .btn{width:82px;height:20px;margin-top:14px}

/* stats */
.stat{position:absolute;top:3082px;display:flex;gap:12px;align-items:center}
.stat .num{font-size:20px;color:var(--ink);font-weight:400}
.stat .num sup{font-size:9px}
.stat .cap{font-size:7px;font-weight:700;letter-spacing:1.2px;text-transform:uppercase}

/* testimonial */
.testi-band{top:3302px;left:0;width:1200px;height:308px;background:var(--mist)}
.testi-card{top:3193px;left:243px;width:356px;height:356px;background:var(--white);box-shadow:0 4px 18px rgba(0,0,0,.06);padding:22px 17px}
.testi-card h2{font-size:21px;line-height:27px;color:var(--green);margin:8px 0 14px}
.testi-card p{font-size:8px;line-height:13px;color:var(--muted)}
.quote{left:634px;top:3365px;width:290px}
.quote .stars{color:var(--green);font-size:11px;letter-spacing:3px}
.quote p{font-size:8.5px;line-height:14px;color:var(--muted);margin:14px 0 18px}
.author{display:flex;gap:12px;align-items:center}
.author b{font-size:9px;color:var(--green);display:block}
.author span{font-size:7px;color:var(--muted)}

/* footer */
.site-footer{top:4377px;left:0;width:1200px;height:442px;background:var(--forest);color:#d8e6d3}
.footer-brand{position:absolute;left:0;width:1200px;top:78px;display:flex;justify-content:center;align-items:center;gap:7px;font-family:"Rubik",sans-serif;font-weight:700;font-size:15px;color:var(--lime)}
.footer-brand .dot{width:16px;height:16px;border-radius:50%;background:var(--lime)}
.footer-about{position:absolute;top:127px;width:1200px;text-align:center;font-size:8.5px;line-height:13px}
.footer-links{position:absolute;top:181px;width:1200px;display:flex;justify-content:center;gap:15px;font-size:8px}
.footer-rule{position:absolute;top:212px;left:249px;width:702px;border-top:1px solid rgba(255,255,255,.14)}
.fcol{position:absolute;top:263px}
.fcol h4{font-family:"Rubik",sans-serif;font-size:12px;color:var(--lime);margin-bottom:10px}
.fitem{display:flex;gap:12px;margin-bottom:10px;font-size:7.5px;line-height:11px}
.fitem b{color:var(--lime);font-size:9px;display:block}
.fine{font-size:7px;line-height:11px;margin-bottom:6px;display:flex;gap:6px}
.newsletter input{display:none}
.footer-bottom{position:absolute;top:410px;left:258px;width:692px;display:flex;justify-content:space-between;align-items:center;font-size:7px}
.social{display:flex;gap:12px}
.social i{width:9px;height:9px;border-radius:50%;background:#d8e6d3;display:block}
</style>
</head>
<body>

<div class="abs admin-bar"><span>My Site</span><span>Customize</span><span>+ New</span><span>Edit Page</span><span>Purge Cache</span><span class="right">Howdy, editor</span></div>

<header class="abs site-header">
  <div class="brand"><span class="dot"></span>Plover Meadow</div>
  <nav class="nav"><span class="active">Homepage</span><span>Divisions ▾</span><span>Services ▾</span><span>About us</span><span>Gallery</span><span>Contact</span></nav>
  <div class="header-phone">
    <svg width="11" height="11" viewBox="0 0 24 24" fill="none" stroke="#7a7f7a" stroke-width="2"><path d="M5 3h4l2 5-3 2a11 11 0 0 0 6 6l2-3 5 2v4a2 2 0 0 1-2 2A17 17 0 0 1 3 5a2 2 0 0 1 2-2z"/></svg>1-555-310-4420
  </div>
  <span class="btn header-cta">Get an appointment</span>
</header>

<section class="abs hero" role="img" aria-label="Lawn sprinkler spraying water across a green lawn"></section>
<div class="abs hero-band"></div>
<h1 class="abs hero-title">Let us help create the<br>yard of your dreams.</h1>
<p class="abs hero-sub">Congue pulvinar augue vel duis sem aliquam volutpat amet quisque interdum montes odio</p>
<div class="abs hero-btns"><span class="btn">Get in touch</span><span class="btn ghost">Discover more</span></div>

<section class="abs quick">
  <div class="quick-call">
    <svg width="28" height="28" viewBox="0 0 24 24" fill="none" stroke="#fff" stroke-width="1.5"><path d="M5 3h4l2 5-3 2a11 11 0 0 0 6 6l2-3 5 2v4a2 2 0 0 1-2 2A17 17 0 0 1 3 5a2 2 0 0 1 2-2z"/></svg>
    <div class="label">Call Us Now</div>
    <div class="num">1-555-310-4420</div>
  </div>
  <div class="field" style="left:273px;top:30px;width:126px">Name</div>
  <div class="field" style="left:409px;top:30px;width:126px">Phone Number</div>
  <div class="field" style="left:545px;top:30px;width:128px">Email</div>
  <div class="field" style="left:273px;top:64px;width:126px;justify-content:space-between">Select Services <span>▾</span></div>
  <div class="field" style="left:409px;top:64px;width:126px">Select Date</div>
  <span class="btn" style="position:absolute;left:545px;top:64px;width:128px;height:24px">Get a quote</span>
  <div class="rule"></div>
  <div class="note">Leo vulputate orci habitant molestie semper commodo malesuada aliquam</div>
</section>

<!-- about -->
<div class="abs about-text">
  <div class="eyebrow">About us</div>
  <h2>Dedicated to Healthy Life and Environment</h2>
  <p class="body" style="font-size:9px;line-height:15px">Lorem ipsum dolor sit amet, consectetur adipiscing elit. Ut elit tellus, luctus nec ullamcorper mattis, pulvinar dapibus leo.</p>
  <span class="btn">Discover more</span>
</div>
<div class="photo" role="img" aria-label="Garden waterfall with rocks and red flowers" style="left:627px;top:770px;width:303px;height:180px;background:linear-gradient(135deg,#3f6a2e,#7b8c6a 55%,#c4545a)"></div>
<div class="photo" role="img" aria-label="Stone garden path through greenery" style="left:560px;top:836px;width:167px;height:183px;background:linear-gradient(180deg,#6f8f4e,#a89a84 60%,#7d7468);box-shadow:0 6px 16px rgba(0,0,0,.18)"></div>

<!-- team -->
<section class="abs team"></section>
<div class="photo" role="img" aria-label="Team member in red sweater and striped apron" style="left:275px;top:1182px;width:194px;height:291px;background:linear-gradient(180deg,#6d7f55,#a8463f 70%,#7a2e2a)"></div>
<div class="photo" role="img" aria-label="Team member in brown gardening apron" style="left:481px;top:1182px;width:194px;height:291px;background:linear-gradient(180deg,#8b9a76,#d8d2c4 55%,#6e4a34)"></div>
<div class="abs team-text">
  <div class="eyebrow">Meet the team</div>
  <h2>Every problem is an opportunity being mishandled.</h2>
  <p class="body" style="font-size:9px;line-height:15px">Lorem ipsum dolor sit amet, consectetur adipiscing elit. Ut elit tellus, luctus nec ullamcorper mattis, pulvinar dapibus leo.</p>
  <span class="btn">Meet all team</span>
</div>

<!-- services -->
<div class="abs section-head" style="top:1608px">
  <div class="eyebrow">Our services</div>
  <h2>Affordable Price and Reasonable Service</h2>
</div>
<div class="photo" role="img" aria-label="Two gardeners working under a pergola" style="left:270px;top:1761px;width:303px;height:203px;background:linear-gradient(135deg,#8a6248,#3f7a2c 50%,#2d5a1e)"></div>
<div class="photo" role="img" aria-label="Sprinkler watering a lawn" style="left:202px;top:1826px;width:168px;height:184px;background:linear-gradient(180deg,#5c7a44,#4f9a2a 60%,#3d8a20);box-shadow:0 6px 16px rgba(0,0,0,.15)"></div>

<div class="service" style="left:612px;top:1753px">
  <svg viewBox="0 0 24 24" fill="none" stroke="#eea53a" stroke-width="1.6"><circle cx="12" cy="12" r="9"/><circle cx="12" cy="12" r="4"/></svg>
  <h3>Maintenance</h3><p>Plover Meadow's mow residential homes, field mowing/brush hogging, small to large commercial properties, including Home Owner Associations.</p>
</div>
<div class="service" style="left:786px;top:1753px">
  <svg viewBox="0 0 24 24" fill="none" stroke="#eea53a" stroke-width="1.6"><rect x="4" y="4" width="16" height="16"/><path d="M4 16l5-5 4 4 3-3 4 4"/></svg>
  <h3>Landscaping</h3><p>Plover Meadow will design and install the landscape of your choice. Our professional designers will take into account your personal taste.</p>
</div>
<div class="service" style="left:612px;top:1923px">
  <svg viewBox="0 0 24 24" fill="none" stroke="#eea53a" stroke-width="1.6"><path d="M4 20h16M7 20V9l5-5 5 5v11"/></svg>
  <h3>Fertilization</h3><p>Plover Meadow will treat your lawn with several different fertilization applications. Each fertilization program will be dependent upon your turf type.</p>
</div>
<div class="service" style="left:786px;top:1923px">
  <svg viewBox="0 0 24 24" fill="none" stroke="#eea53a" stroke-width="1.6"><rect x="8" y="3" width="8" height="6"/><path d="M12 9v12M7 14h10"/></svg>
  <h3>Irrigation</h3><p>Plover Meadow continually consults with leaders in the irrigation industry to remain on new irrigation designs to maximize area coverage.</p>
</div>
<div class="service" style="left:612px;top:2093px">
  <svg viewBox="0 0 24 24" fill="none" stroke="#eea53a" stroke-width="1.6"><path d="M12 3v12M8 21h8l-2-6h-4z"/></svg>
  <h3>Turf Management</h3><p>Plover Meadow has provided beautiful green lawns to our customers, from homeowners, to commercial sites.</p>
</div>
<div class="service" style="left:786px;top:2093px">
  <svg viewBox="0 0 24 24" fill="none" stroke="#eea53a" stroke-width="1.6"><path d="M4 20l9-9M11 5l8 8-3 3-8-8z"/></svg>
  <h3>Hardscaping</h3><p>Plover Meadow design team can create brick patios, sidewalks, and retaining walls to help enhance the look of your landscape.</p>
</div>

<!-- offer -->
<section class="abs offer" role="img" aria-label="Gardener in cap and overalls trimming a hedge"></section>
<div class="abs offer-box">
  <div class="eyebrow" style="color:var(--lime)">Special offer</div>
  <h2>50% Off<br>All Gardening Services</h2>
  <p>Add a strong one liner supporting the heading above and giving users a reason to click on the button below.</p>
  <span class="btn">Apply now</span>
</div>

<!-- trust -->
<div class="abs section-head" style="top:2933px">
  <div class="eyebrow">They trust us</div>
  <h2>Over 5,000+ commercial and residential complete overhaul</h2>
  <p style="font-size:8.5px;color:var(--muted);margin-top:14px">Finibus nostra ullamcorper lacinia metus lacus imperdiet placerat facilisis. Urna fusce blandit eros porttitor hendrerit nascetur tempor.</p>
</div>
<div class="stat" style="left:258px">
  <svg width="32" height="40" viewBox="0 0 24 30" fill="none" stroke="#eea53a" stroke-width="1.4"><rect x="3" y="4" width="18" height="24"/><path d="M8 12h8M8 17h8M8 22h5M9 4V2h6v2"/></svg>
  <div><div class="num">5,124<sup>+</sup></div><div class="cap">Project done</div></div>
</div>
<div class="stat" style="left:432px">
  <svg width="38" height="38" viewBox="0 0 24 24" fill="none" stroke="#eea53a" stroke-width="1.4"><path d="M3 12l9-8 9 8v9H3z"/><path d="M9 21v-6h6v6"/></svg>
  <div><div class="num">5,124<sup>+</sup></div><div class="cap">Happy client</div></div>
</div>
<div class="stat" style="left:612px">
  <svg width="32" height="40" viewBox="0 0 24 30" fill="none" stroke="#eea53a" stroke-width="1.4"><circle cx="12" cy="8" r="5"/><path d="M4 28v-8a8 8 0 0 1 16 0v8"/></svg>
  <div><div class="num">5,124<sup>+</sup></div><div class="cap">Gardeners</div></div>
</div>
<div class="stat" style="left:782px">
  <svg width="38" height="38" viewBox="0 0 24 24" fill="none" stroke="#eea53a" stroke-width="1.4"><circle cx="12" cy="12" r="9"/><circle cx="12" cy="12" r="5"/></svg>
  <div><div class="num">5,124<sup>+</sup></div><div class="cap">Awards</div></div>
</div>

<!-- testimonial -->
<section class="abs testi-band"></section>
<div class="abs testi-card">
  <div class="eyebrow">Testimonial</div>
  <h2>What Client Tell About Our Services</h2>
  <p>Aenean elit duis litora platea euismod tincidunt amet libero ipsum curabitur adipiscing morbi leo risus blandit.</p>
  <div role="img" aria-label="Group of happy clients sitting in a park" style="margin-top:20px;height:137px;background:linear-gradient(135deg,#5f9a3e,#b84a4a 45%,#3f7a5a)"></div>
</div>
<div class="abs quote">
  <div class="stars">★★★★☆</div>
  <p>Class facilisi hendrerit arcu nibh phasellus egestas proin semper fermentum efficitur malesuada nullam netus libero velit consectetur sodales pretium fames himenaeos fusce viverra</p>
  <div class="author">
    <svg width="30" height="34" viewBox="0 0 24 28" fill="none" stroke="#eea53a" stroke-width="1.3"><path d="M3 4h18l-6 6v16h-4V10z"/></svg>
    <div><b>Elric Danvers</b><span>Property Agent</span></div>
  </div>
</div>

<!-- gallery -->
<div class="abs section-head" style="top:3692px">
  <div class="eyebrow">Featured capture</div>
  <h2>Awesome Gallery</h2>
  <p style="font-size:9px;line-height:15px;color:var(--muted);margin:12px auto 0;width:350px">Lorem ipsum dolor sit amet, consectetur adipiscing elit. Ut elit tellus, luctus nec ullamcorper mattis, pulvinar dapibus leo.</p>
</div>
<div class="photo" role="img" aria-label="Flower-lined garden wall and curved paving" style="left:6px;top:3861px;width:393px;height:221px;background:linear-gradient(135deg,#4a5a3a,#8a7a5a 55%,#b7a06a)"></div>
<div class="photo" role="img" aria-label="Garden waterfall among red flowers" style="left:404px;top:3861px;width:393px;height:221px;background:linear-gradient(160deg,#3f6a2e,#8a8c7a 55%,#c4545a)"></div>
<div class="photo" role="img" aria-label="Gardeners carrying flower trays" style="left:801px;top:3861px;width:393px;height:221px;background:linear-gradient(135deg,#7aa24a,#2f5a26 55%,#9ab86a)"></div>
<div class="photo" role="img" aria-label="Stone garden wall with flower beds" style="left:6px;top:4087px;width:393px;height:221px;background:linear-gradient(180deg,#8aa06a,#9aa6a4 50%,#5f8a2e)"></div>
<div class="photo" role="img" aria-label="Rolled turf laid over soil" style="left:404px;top:4087px;width:393px;height:221px;background:linear-gradient(120deg,#6a4a32,#8a6a4a 50%,#4f8a2a)"></div>
<div class="photo" role="img" aria-label="Sprinkler watering a sunny lawn" style="left:801px;top:4087px;width:393px;height:221px;background:linear-gradient(180deg,#3a5a2a,#5f8a3a 50%,#4fa02a)"></div>

<!-- footer -->
<footer class="abs site-footer">
  <div class="footer-brand"><span class="dot"></span>Plover Meadow</div>
  <p class="footer-about">Lorem ipsum dolor sit amet, consectetur adipiscing elit. Ut elit tellus, luctus nec ullamcorper<br>mattis, pulvinar dapibus leo.</p>
  <div class="footer-links"><span>About Us</span><span>Leadership</span><span>Career</span><span>Partner</span><span>News &amp; Article</span><span>Legal Notice</span></div>
  <div class="footer-rule"></div>

  <div class="fcol" style="left:271px;width:170px">
    <div class="fitem"><svg width="18" height="18" viewBox="0 0 24 24" fill="none" stroke="#d8e6d3" stroke-width="1.5"><rect x="5" y="3" width="14" height="18"/><path d="M9 7h2M13 7h2M9 11h2M13 11h2"/></svg><div><b>Headquarter</b>418 Fieldstone Ave,<br>Ames - Iowa</div></div>
    <div class="fitem"><svg width="18" height="18" viewBox="0 0 24 24" fill="none" stroke="#d8e6d3" stroke-width="1.5"><rect x="3" y="5" width="18" height="14"/><path d="M3 5l9 8 9-8"/></svg><div><b>Email Us</b>hello@plovermeadowco.com</div></div>
    <div class="fitem"><svg width="18" height="18" viewBox="0 0 24 24" fill="none" stroke="#d8e6d3" stroke-width="1.5"><path d="M5 3h4l2 5-3 2a11 11 0 0 0 6 6l2-3 5 2v4a2 2 0 0 1-2 2A17 17 0 0 1 3 5a2 2 0 0 1 2-2z"/></svg><div><b>Call Us</b>+1 555 310 4421</div></div>
  </div>
  <div class="fcol" style="left:485px;width:130px">
    <h4>Working Hours</h4>
    <div class="fine"><span>▣</span>Mon-Fri: 7:00 AM – 8:00 PM</div>
    <div class="fine"><span>▣</span>Saturday: 9:00 AM – 5:00 PM</div>
    <div class="fine"><span>▣</span>Sunday: Closed</div>
  </div>
  <div class="fcol newsletter" style="left:660px;width:262px">
    <h4>Newsletter</h4>
    <div class="fine" style="font-size:6.5px">Sign up our newsletter to get update information, promotion and insight.</div>
    <div style="margin-top:14px;height:20px;background:#fff;color:#9aa09a;font-size:7px;display:flex;align-items:center;padding:0 8px">Email</div>
    <span class="btn" style="display:flex;margin-top:4px;height:18px;background:var(--green);color:#fff">Subscribe</span>
  </div>

  <div class="footer-bottom">
    <div class="social"><i></i><i></i><i></i></div>
    <span>© 2021 Plover Meadow | All rights reserved | Made with care</span>
  </div>
</footer>

</body>
</html>
```